Gravaloop bottle design

We're a small company looking for someone to help with our bottle design. We provide a sauce that will boost the flavor of packaged ramen. We're looking for a label that will stand out. I'm attaching some of the labels we like and some that I've made.

```html
<!DOCTYPE html>
<html lang="en">
<head>
<meta charset="utf-8">
<title>Gravaloop Ramen Sauce – Bottle Label</title>
<link rel="stylesheet" href="https://fonts.googleapis.com/css2?family=Ubuntu:wght@400;500&family=Montserrat:wght@300;500&display=swap">
<style>
  :root {
    --bg-deep: #0d0202;
    --bg-glow: #2b0600;
    --label-black: #050505;
    --gold-line: #b07a12;
    --gold-light: #f2d21c;
    --gold-dark: #a8620e;
    --brand-red: #d0101a;
    --dish-cream: #cfcbbf;
    --sauce-brown: #3a0c04;
  }
  * { margin: 0; padding: 0; box-sizing: border-box; }
  html, body {
    width: 1161px;
    height: 1200px;
    overflow: hidden;
  }
  body {
    background: radial-gradient(ellipse at 40% 50%, var(--bg-glow) 0%, #1a0301 45%, var(--bg-deep) 100%);
    font-family: "Ubuntu", sans-serif;
    position: relative;
  }
  .label {
    position: absolute;
    left: 459px;
    top: 459px;
    width: 236px;
    height: 557px;
    background: var(--label-black);
    border: 1.5px solid var(--gold-line);
    border-radius: 12px;
    text-align: center;
  }
  .brand-name {
    position: absolute;
    top: 62px;
    width: 100%;
    font-family: "Ubuntu", sans-serif;
    font-weight: 400;
    font-size: 28px;
    line-height: 34px;
    letter-spacing: 1.5px;
    color: var(--brand-red);
  }
  .product-type {
    position: absolute;
    top: 114px;
    width: 100%;
    font-family: "Montserrat", sans-serif;
    font-weight: 500;
    font-size: 7.5px;
    line-height: 10px;
    letter-spacing: 2.5px;
    color: var(--brand-red);
  }
  .divider {
    position: absolute;
    top: 129px;
    left: 48px;
    width: 140px;
    height: 8px;
  }
  .product-meta {
    position: absolute;
    top: 144px;
    width: 100%;
    font-family: "Montserrat", sans-serif;
    font-weight: 500;
    font-size: 5.5px;
    line-height: 8px;
    letter-spacing: 1.5px;
    color: var(--brand-red);
  }
  .product-title {
    position: absolute;
    top: 196px;
    width: 100%;
    font-family: "Ubuntu", sans-serif;
    font-weight: 500;
    font-size: 46px;
    line-height: 46px;
    background: linear-gradient(90deg, var(--gold-dark) 20%, var(--gold-light) 45%, var(--gold-light) 60%, var(--gold-dark) 82%);
    -webkit-background-clip: text;
    background-clip: text;
    color: transparent;
  }
  .dish-photo {
    position: absolute;
    top: 306px;
    left: 30px;
    width: 176px;
    height: 170px;
    border-radius: 8px;
    background: linear-gradient(180deg, var(--dish-cream) 0%, #7d5a48 50%, var(--sauce-brown) 100%);
  }
  .authenticity {
    position: absolute;
    top: 500px;
    width: 100%;
    display: flex;
    justify-content: center;
    align-items: flex-end;
    gap: 2px;
    font-family: "Montserrat", sans-serif;
    font-weight: 300;
    font-size: 13px;
    line-height: 16px;
    letter-spacing: 0.5px;
    color: var(--gold-line);
  }
  .tick-icon { width: 18px; height: 18px; }
</style>
</head>
<body>
  <main class="label">
    <div class="brand-name">Gravaloop</div>
    <div class="product-type">RAMEN SAUCE</div>
    <svg class="divider" viewBox="0 0 140 8" aria-hidden="true">
      <line x1="4" y1="4" x2="136" y2="4" stroke="#d0101a" stroke-width="1"/>
      <circle cx="4" cy="4" r="2.5" fill="none" stroke="#d0101a" stroke-width="0.8"/>
      <circle cx="136" cy="4" r="2.5" fill="none" stroke="#d0101a" stroke-width="0.8"/>
    </svg>
    <div class="product-meta">OHIO'S BEST<br>11.2 FL OZ (330 ML)</div>
    <h1 class="product-title">Soy<br>Sauce</h1>
    <div class="dish-photo" role="img" aria-label="Photo of a small white dipping dish filled with soy sauce"></div>
    <div class="authenticity">
      <span>100%</span>
      <svg class="tick-icon" viewBox="0 0 20 20" aria-hidden="true">
        <path d="M2 11 L8 18 L19 2" fill="none" stroke="#d9a514" stroke-width="2.2" stroke-linecap="round" stroke-linejoin="round"/>
      </svg>
      <span>ORIGINAL</span>
    </div>
  </main>
</body>
</html>
```